Process Roadmap for Interior Design Firm

We are looking to ramp up the design appeal of our current process roadmap to be very visually interesting, while staying informative and descriptive about our process.

Target Market(s)

In-house Clients

Industry/Entity Type

Interior Design Firm focused on sustainable and holistic design.

Other font styles liked:
• raleway

Requirements
Must have
• 1.) it would be nice if the graphic provided a more clear indication of the “journey” from one step to the next, so that there was a clear sense of the progression (such that we are directing the viewer) 2.). We would want it to fit on an 8.5”x11” page (the page could be horizontal when we have the Calm Compass formatted out with the testimonials) (in addition to the testimonials, we may also want to have the detailed descriptions of each step of the process presented below the graphic, so that the graphic is cleaner) 3.) ideally the graphic is clear and simple enough to also be used on our Bi-Weekly Client Updates, which will be typed updates for clients re their project budgets, schedule and scope. The Calm Compass graphic (without all the testimonials) would be at the end of the update, and would fit on the page horizontally at the bottom, perhaps in a space which is 7.5”w x 4”h or so.
Should not have
• bold or bright colors. Natural neutrals are preferred, such as the ones featured on the provided graphic.

```html
<!DOCTYPE html>
<html lang="en">
<head>
<meta charset="utf-8">
<title>LHI Calm Compass – Process Roadmap</title>
<link href="https://fonts.googleapis.com/css2?family=Oswald:wght@600&family=Poppins:wght@600;700&family=Raleway:wght@500;600&display=swap" rel="stylesheet">
<style>
  :root{
    --backdrop:#b3b3b3;
    --paper:#ffffff;
    --tan:#bdae82;
    --tan-light:#e0d4ab;
    --gold:#b8963f;
    --heading:#85774f;
    --body:#3f3f3f;
    --pattern:#e4d3a4;
  }
  *{margin:0;padding:0;box-sizing:border-box}
  html,body{width:1200px;height:1117px;overflow:hidden}
  body{background:var(--backdrop);position:relative;font-family:"Raleway",sans-serif}
  .card{position:absolute;background:var(--paper);overflow:hidden}
  .card--sheet{left:213px;top:94px;width:774px;height:598px}
  .card--update{left:316px;top:720px;width:568px;height:303px}
  .abs{position:absolute}

  .accent-strip{background:var(--tan-light)}
  .brand-name{font-family:"Raleway",sans-serif;font-weight:600;color:var(--gold);line-height:1;white-space:nowrap;text-align:center}
  .divider{background:var(--tan)}
  .title{font-family:"Oswald",sans-serif;font-weight:600;text-align:right;line-height:1;letter-spacing:-.5px;white-space:nowrap}
  .title__top{color:var(--tan)}
  .title__bottom{color:var(--tan-light)}

  .band{background:var(--tan)}
  .panel{background:var(--paper);border:2px solid var(--tan);border-bottom:none}
  .chevrons{position:absolute;left:0;overflow:visible}
  .chevron--dark{fill:var(--tan)}
  .chevron--light{fill:var(--tan-light)}
  .chevron-num{font-family:"Poppins",sans-serif;font-weight:700;fill:#fff;text-anchor:middle;dominant-baseline:central}

  .step{position:absolute;text-align:center}
  .step__icon{display:block;margin:0 auto;color:var(--tan)}
  .step__name{font-family:"Poppins",sans-serif;font-weight:600;color:var(--heading);white-space:nowrap;line-height:1}
  .step__text{color:var(--body);font-weight:500}
  .step__text span{display:block}
  .step__text span + span{margin-top:var(--gap)}

  .card--sheet .step{top:281px;width:82px}
  .card--sheet .step__icon{width:31px;height:31px}
  .card--sheet .step__name{font-size:15px;margin:9px -20px 0}
  .card--sheet .step__text{font-size:8px;line-height:9.2px;margin-top:7px;--gap:9px}

  .card--update .step{top:150px;width:60px}
  .card--update .step__icon{width:23px;height:23px}
  .card--update .step__name{font-size:10.5px;margin:8px -16px 0}
  .card--update .step__text{font-size:5.4px;line-height:6.8px;margin-top:6px;--gap:6.8px}

  .testimonials-tab{left:128px;top:463px;width:516px;height:33px}
  .testimonials-tab svg{position:absolute;inset:0}
  .testimonials-tab h2{position:relative;font-family:"Poppins",sans-serif;font-weight:700;color:#fff;font-size:17.5px;text-align:center;line-height:33px;letter-spacing:.3px}
  .testimonial{top:517px;width:140px;color:#fff;font-family:"Poppins",sans-serif;font-weight:600;font-size:11.4px;line-height:12.3px}
  .testimonial-rule{top:521px;width:1.5px;height:46px;background:#fff}

  .edge-pattern{background:var(--pattern)}
</style>
</head>
<body>

<svg width="0" height="0" style="position:absolute" aria-hidden="true">
  <defs>
    <symbol id="icon-listen" viewBox="0 0 32 32">
      <path fill="currentColor" d="M14 2c-6 0-10 4.3-10 10 0 3.4 1.6 5.3 2.8 7 1 1.4 1.2 2.6 1.2 4.5C8 28 10.5 30.5 14 30.5c3 0 5-2 5.4-4.6l-2.6-.4c-.3 1.5-1.3 2.4-2.8 2.4-2 0-3.3-1.5-3.3-4.4 0-2.6-.6-4.200-1.8-5.9C7.8 16.3 6.8 15 6.8 12c0-4.2 3-7.3 7.2-7.3s7 3 7 7h2.7C23.7 6.2 19.7 2 14 2z"/>
      <path fill="currentColor" d="M14 8c-2.3 0-4 1.8-4 4h2.4c0-1 .7-1.7 1.6-1.7s1.6.7 1.6 1.7c0 1.3-1.2 1.7-1.2 3.6v2h2.4v-2c0-1 1.2-1.8 1.2-3.6 0-2.2-1.7-4-4-4z"/>
      <path stroke="currentColor" stroke-width="1.8" stroke-linecap="round" d="M24 9l5-3M25 14h6M24 19l5 3"/>
    </symbol>
    <symbol id="icon-vision" viewBox="0 0 32 32">
      <path fill="currentColor" d="M16 7C8.5 7 3 13 1 16c2 3 7.5 9 15 9s13-6 15-9c-2-3-7.5-9-15-9zm0 15a6 6 0 1 1 0-12 6 6 0 0 1 0 12z"/>
      <circle cx="16" cy="16" r="2.8" fill="currentColor"/>
    </symbol>
    <symbol id="icon-plan" viewBox="0 0 32 32">
      <rect x="2" y="3" width="28" height="3" fill="currentColor"/>
      <rect x="4" y="6" width="24" height="17" fill="none" stroke="currentColor" stroke-width="2.2"/>
      <path fill="none" stroke="currentColor" stroke-width="1.8" d="M8 19l5-5 3 3 6-6M16 23l-4 7M16 23l4 7M16 23v6"/>
      <path stroke="currentColor" stroke-width="1.5" d="M21 16l4 4M25 16l-4 4"/>
    </symbol>
    <symbol id="icon-design" viewBox="0 0 32 32">
      <g fill="currentColor">
        <rect x="13" y="-2" width="6" height="36" rx="1" transform="rotate(45 16 16)"/>
        <path d="M13 3h6v22l-3 5-3-5z" transform="rotate(-45 16 16)"/>
      </g>
      <path stroke="#fff" stroke-width="1.2" d="M9 17l2 2M12 14l2 2M18 8l2 2M21 5l2 2"/>
    </symbol>
    <symbol id="icon-manage" viewBox="0 0 32 32">
      <circle cx="12" cy="7" r="5.5" fill="currentColor"/>
      <path fill="currentColor" d="M2 29v-5c0-5 4.5-9 10-9 3 0 5 1 6.5 2.5V29z"/>
      <circle cx="24" cy="24" r="4.2" fill="none" stroke="currentColor" stroke-width="3.2" stroke-dasharray="2.2 1.1"/>
      <circle cx="24" cy="24" r="3.2" fill="currentColor"/>
      <circle cx="24" cy="24" r="1.4" fill="#fff"/>
    </symbol>
    <symbol id="icon-install" viewBox="0 0 32 32">
      <circle cx="16" cy="16" r="12" fill="none" stroke="currentColor" stroke-width="5" stroke-dasharray="4.2 3.3"/>
      <circle cx="16" cy="16" r="10" fill="currentColor"/>
      <circle cx="16" cy="16" r="6.8" fill="#fff"/>
      <path fill="currentColor" d="M20 10a4 4 0 0 0-4.8 5L10 20.2l1.8 1.8 5.2-5.2A4 4 0 0 0 22 12l-2 2-2-2z"/>
    </symbol>
    <symbol id="icon-complete" viewBox="0 0 32 32">
      <rect x="3" y="3" width="26" height="26" rx="2.5" fill="currentColor"/>
      <path fill="none" stroke="#fff" stroke-width="3.6" stroke-linecap="square" d="M9 16l5 5 9-10"/>
    </symbol>
  </defs>
</svg>

<!-- Letter-size roadmap sheet with testimonials -->
<section class="card card--sheet" aria-label="LHI Calm Compass roadmap with testimonials">
  <div class="abs accent-strip" style="left:470px;top:0;width:304px;height:18px"></div>

  <div class="abs brand-name" style="left:40px;top:96px;width:360px;font-size:24px">Linden Hale Interiors</div>

  <div class="abs divider" style="left:414px;top:27px;width:3px;height:159px"></div>

  <div class="abs title title__top" style="right:47px;top:52px;font-size:64px">LHI Calm</div>
  <div class="abs title title__bottom" style="right:47px;top:111px;font-size:84px">Compass</div>

  <div class="abs band" style="left:12px;top:423px;width:750px;height:161px"></div>
  <div class="abs panel" style="left:27px;top:243px;width:718px;height:220px"></div>

  <svg class="chevrons" style="top:220px" width="774" height="50" viewBox="0 0 774 50" aria-hidden="true">
    <g>
      <polygon class="chevron--dark"  points="41,0 130,0 145,25 130,50 41,50 56,25"/>
      <polygon class="chevron--light" points="139,0 228,0 243,25 228,50 139,50 154,25"/>
      <polygon class="chevron--dark"  points="237,0 326,0 341,25 326,50 237,50 252,25"/>
      <polygon class="chevron--light" points="335,0 424,0 439,25 424,50 335,50 350,25"/>
      <polygon class="chevron--dark"  points="433,0 522,0 537,25 522,50 433,50 448,25"/>
      <polygon class="chevron--light" points="531,0 620,0 635,25 620,50 531,50 546,25"/>
      <polygon class="chevron--dark"  points="629,0 718,0 733,25 718,50 629,50 644,25"/>
    </g>
    <g class="chevron-num" font-size="25">
      <text x="91" y="26">1</text><text x="189" y="26">2</text><text x="287" y="26">3</text><text x="385" y="26">4</text><text x="483" y="26">5</text><text x="581" y="26">6</text><text x="679" y="26">7</text>
    </g>
  </svg>

  <div class="step" style="left:51px"><svg class="step__icon"><use href="#icon-listen"/></svg><h3 class="step__name">Listening</h3><p class="step__text"><span>Listening to our clients, their land, and their home.</span><span>Identifying their needs, challenges, wishes, and dreams.</span></p></div>
  <div class="step" style="left:149px;width:84px"><svg class="step__icon"><use href="#icon-vision"/></svg><h3 class="step__name">Visioning</h3><p class="step__text"><span>Facilitating a guided visioning process to clarify the deepest intention, true purpose, and highest potential for their home and their future within it.</span></p></div>
  <div class="step" style="left:245px;width:86px"><svg class="step__icon"><use href="#icon-plan"/></svg><h3 class="step__name">Planning</h3><p class="step__text"><span>Turning our client's vision into a clearly defined scope, budget, and timeline.</span><span>Mapping out the steps for making their dream a reality.</span><span>Setting a meeting schedule from start to finish.</span></p></div>
  <div class="step" style="left:345px"><svg class="step__icon"><use href="#icon-design"/></svg><h3 class="step__name">Designing</h3><p class="step__text"><span>Following the schedule through the design phases from initial design concepts, technical drawings and the selection of all finishes, fixtures, and furnishings.</span></p></div>
  <div class="step" style="left:443px"><svg class="step__icon"><use href="#icon-manage"/></svg><h3 class="step__name">Managing</h3><p class="step__text"><span>Coordinating with clients, builders, architects, and vendors to ensure that the design is executed with excellence, and the construction and furnishings are on-time and on-budget.</span></p></div>
  <div class="step" style="left:539px;width:86px"><svg class="step__icon"><use href="#icon-install"/></svg><h3 class="step__name">Installing</h3><p class="step__text"><span>Overseeing the inspection, installation, and arrangement of all furnishings, lighting, artwork, and decorative items.</span><span>Taking care of every last detail.</span></p></div>
  <div class="step" style="left:639px"><svg class="step__icon"><use href="#icon-complete"/></svg><h3 class="step__name">Completing</h3><p class="step__text"><span>Fixing any issues or defects.</span><span>Follow up on all remaining items.</span><span>Completing the final finishing touches to our client's full and total satisfaction.</span></p></div>

  <div class="abs testimonials-tab">
    <svg width="516" height="33" viewBox="0 0 516 33" aria-hidden="true"><polygon points="0,0 516,0 498,33 18,33" fill="var(--tan-light)"/></svg>
    <h2>TESTIMONIALS</h2>
  </div>

  <p class="abs testimonial" style="left:59px">Linden to send over testimonials for fill this space-three or four columns of testimonials</p>
  <div class="abs testimonial-rule" style="left:211px"></div>
  <p class="abs testimonial" style="left:233px">Linden to send over testimonials for fill this space-three or four columns of testimonials</p>
  <div class="abs testimonial-rule" style="left:383px"></div>
  <p class="abs testimonial" style="left:406px">Linden to send over testimonials for fill this space-three or four columns of testimonials</p>
  <div class="abs testimonial-rule" style="left:560px"></div>
  <p class="abs testimonial" style="left:579px">Linden to send over testimonials for fill this space-three or four columns of testimonials</p>
</section>

<!-- Compact roadmap for client updates -->
<section class="card card--update" aria-label="LHI Calm Compass compact roadmap">
  <div class="abs edge-pattern" role="img" aria-label="Gold geometric line pattern border, left edge" style="left:0;top:0;width:48px;height:242px"></div>
  <div class="abs edge-pattern" role="img" aria-label="Gold geometric line pattern border, right edge" style="left:520px;top:0;width:48px;height:242px"></div>
  <div class="abs band" style="left:0;top:242px;width:568px;height:61px"></div>

  <div class="abs brand-name" style="left:62px;top:46px;width:200px;font-size:13px">Linden Hale Interiors</div>

  <div class="abs divider" style="left:270px;top:15px;width:2px;height:72px"></div>

  <div class="abs title title__top" style="right:78px;top:13px;font-size:43px">LHI Calm</div>
  <div class="abs title title__bottom" style="right:78px;top:51px;font-size:47px">Compass</div>

  <div class="abs panel" style="left:17px;top:129px;width:536px;height:157px;border-width:2px"></div>

  <svg class="chevrons" style="top:104px" width="568" height="36" viewBox="0 0 568 36" aria-hidden="true">
    <g>
      <polygon class="chevron--dark"  points="27,0 94,0 105,18 94,36 27,36 38,18"/>
      <polygon class="chevron--light" points="100,0 167,0 178,18 167,36 100,36 111,18"/>
      <polygon class="chevron--dark"  points="173,0 240,0 251,18 240,36 173,36 184,18"/>
      <polygon class="chevron--light" points="246,0 313,0 324,18 313,36 246,36 257,18"/>
      <polygon class="chevron--dark"  points="319,0 386,0 397,18 386,36 319,36 330,18"/>
      <polygon class="chevron--light" points="392,0 459,0 470,18 459,36 392,36 403,18"/>
      <polygon class="chevron--dark"  points="465,0 532,0 543,18 532,36 465,36 476,18"/>
    </g>
    <g class="chevron-num" font-size="18">
      <text x="64" y="19">1</text><text x="137" y="19">2</text><text x="211" y="19">3</text><text x="284" y="19">4</text><text x="357" y="19">5</text><text x="430" y="19">6</text><text x="503" y="19">7</text>
    </g>
  </svg>

  <div class="step" style="left:35px"><svg class="step__icon"><use href="#icon-listen"/></svg><h3 class="step__name">Listening</h3><p class="step__text"><span>Listening to our clients, their land, and their home.</span><span>Identifying their needs, challenges, wishes, and dreams.</span></p></div>
  <div class="step" style="left:107px"><svg class="step__icon"><use href="#icon-vision"/></svg><h3 class="step__name">Visioning</h3><p class="step__text"><span>Facilitating a guided visioning process to clarify the deepest intention, true purpose, and highest potential for their home and their future within it.</span></p></div>
  <div class="step" style="left:181px"><svg class="step__icon"><use href="#icon-plan"/></svg><h3 class="step__name">Planning</h3><p class="step__text"><span>Turning our client's vision into a clearly defined scope, budget, and timeline.</span><span>Mapping out the steps for making their dream a reality.</span><span>Setting a meeting schedule from start to finish.</span></p></div>
  <div class="step" style="left:254px"><svg class="step__icon"><use href="#icon-design"/></svg><h3 class="step__name">Designing</h3><p class="step__text"><span>Following the schedule through the design phases from initial design concepts, technical drawings and the selection of all finishes, fixtures, and furnishings.</span></p></div>
  <div class="step" style="left:326px"><svg class="step__icon"><use href="#icon-manage"/></svg><h3 class="step__name">Managing</h3><p class="step__text"><span>Coordinating with clients, builders, architects, and vendors to ensure that the design is executed with excellence, and the construction and furnishings are on-time and on-budget.</span></p></div>
  <div class="step" style="left:400px"><svg class="step__icon"><use href="#icon-install"/></svg><h3 class="step__name">Installing</h3><p class="step__text"><span>Overseeing the inspection, installation, and arrangement of all furnishings, lighting, artwork, and decorative items.</span><span>Taking care of every last detail.</span></p></div>
  <div class="step" style="left:473px"><svg class="step__icon"><use href="#icon-complete"/></svg><h3 class="step__name">Completing</h3><p class="step__text"><span>Fixing any issues or defects.</span><span>Follow up on all remaining items.</span><span>Completing the final finishing touches to our client's full and total satisfaction.</span></p></div>
</section>

</body>
</html>
```